Meal Plan Website Needs New Pages Designed

Sunward Supper Kits is an online, membership based program that delivers weekly meal programs (7 days worth of recipes plus shopping lists) carefully crafted by an expert team of meal planners. All recipes are created to comply with the following macronutrient ratio: 65% healthy fats, 25% lean protein, 10% good carbs.
All recipes are Paleo friendly and a great resource for those individuals who want to correctly implement this type of diet.

We are re-designing our website and need the following pages designed:

· Home page w/ logo
· How it works page
· Get Started! page
· Recipes Page template (these will be the pages on our site that will have recipes)
· Kitchen Essentials Training page (this will be a page with videos and tips + tricks, PDFs, etc)

So 5 total PSDs, 1 for each page.

Target audience: Men and women between the ages of 30 and 60 who want to:
· Eat healthy
· Lose weight
· Follow/Implement the Paleo diet
· Take the guesswork out of preparing delicious AND healthy meals for them and their families
· Know exactly what to eat, what to buy, how to make it

Feelings/Messages we want to communicate through the design:
· “Organic” but elegant look
· Fresh/light/Airy
· Simple but NOT GENERIC
· “I want to get cooking” feeling

Our Stylistic preferences:
· Minimalist with a few bold elements (something in between)
· Easy to visually navigate (enough white space, but not too much)
· There is more to “see” than to “read”

Our Color Preferences:
· Lighter pallet
· Colors that evoke natural woods, granite countertops…
· Stay away from using all dark colors

Our Font Type Preferences:
· Easy to read
· Not more than 3 font types
· Not too rigid
· Not too sophisticated
· Simple with a touch

Examples of Website Designs that we like:
· http://www.brightlarder.example/menus/
· http://stonehearthfare.example/
· https://www.rootkettle.example/

Industry/Entity Type

Shopping

```html
<!DOCTYPE html>
<html lang="en">
<head>
<meta charset="utf-8">
<title>Sunward Supper Kits</title>
<link rel="stylesheet" href="https://fonts.googleapis.com/css2?family=Source+Sans+3:wght@400;600;700&display=swap">
<style>
:root{
  --wood-dark:#4a2c14;
  --wood:#7a4d2a;
  --wood-light:#8f5d35;
  --orange:#ee7f2d;
  --cream:#f4f3ea;
  --ink:#2b2b2b;
  --text:#4a4a4a;
  --muted:#666;
  --rule:#c9c9c9;
  --field:#e9e8df;
  --white:#fff;
}
*{box-sizing:border-box;margin:0;padding:0}
html,body{width:938px;height:1200px;overflow:hidden}
body{position:relative;background:var(--white);font-family:"Source Sans 3",sans-serif;color:var(--ink)}
.abs{position:absolute}

.top-bar{left:0;top:0;width:938px;height:21px;background:var(--wood-dark)}
.account-links{right:168px;top:4px;font-size:9px;color:var(--white);display:flex;gap:9px}
.masthead{left:0;top:21px;width:938px;height:94px;
  background:linear-gradient(90deg,var(--wood) 0%,var(--wood-light) 25%,var(--wood) 45%,var(--wood-light) 70%,var(--wood) 100%)}
.brand{left:115px;top:78px;font-size:20px;font-weight:600;color:var(--white)}
.main-nav{left:484px;top:61px;display:flex;align-items:center;font-size:10px;color:var(--white)}
.main-nav a{color:inherit;text-decoration:none;margin-right:29px}
.main-nav a.active{background:var(--orange);padding:5px 12px;border-radius:2px;margin-right:17px}

.hero{left:0;top:115px;width:938px;height:413px;background:var(--cream)}
.hero-frame{left:103px;top:149px;width:731px;height:336px;border:2px solid #e8e6dc;background:var(--white)}
.hero-photo{position:absolute;inset:0;
  background:radial-gradient(ellipse 70% 45% at 50% 42%,#7fae3b 0%,#5c8f2a 45%,#c9d9b2 80%,#f7f7f4 100%)}
.slider-dots{left:444px;top:502px;display:flex;gap:6px}
.slider-dots span{width:7px;height:7px;border-radius:50%;background:#cfcdc4}
.slider-dots span.on{background:var(--wood-dark)}

.feature{top:566px;width:224px}
.feature-head{display:flex;align-items:center;gap:10px;height:30px}
.feature-head svg{flex:none}
.feature-title{font-size:13.5px;font-weight:700;color:var(--orange)}
.feature p{margin-top:13px;font-size:7.4px;line-height:12.5px;color:var(--text);text-align:justify}

.double-rule{left:103px;width:732px;height:4px;border-top:1px solid var(--rule);border-bottom:1px solid var(--rule)}
.welcome-title{left:0;top:775px;width:938px;text-align:center;font-size:21px;color:var(--orange)}
.welcome-text{left:84px;top:815px;width:770px;text-align:center;font-size:8px;line-height:17.6px;color:var(--ink)}

.footer{left:0;top:961px;width:938px;height:189px;background:var(--cream)}
.footer-heading{top:996px;font-size:14.5px;color:var(--ink)}
.contact-row{left:102px;font-size:8.5px;color:var(--muted);display:flex;align-items:center;gap:10px}
.field{left:285px;width:143px;height:15px;background:var(--field);border:1px solid #dcdbd2;font-size:7px;color:#555;padding:3px 5px}
.small-btn{left:284px;top:1107px;width:41px;height:14px;background:var(--orange);color:var(--white);font-size:7.5px;text-align:center;line-height:14px}
.news-field{left:479px;top:1031px;width:112px;height:20px;background:var(--field);border:1px solid #dcdbd2}
.news-btn{left:591px;top:1031px;width:56px;height:20px;background:var(--orange);color:var(--white);font-size:10px;text-align:center;line-height:20px}
.social{top:1031px;width:21px;height:21px;background:var(--orange)}
.copyright{left:0;top:1170px;width:938px;text-align:center;font-size:8px;color:var(--ink)}
</style>
</head>
<body>

<div class="abs top-bar"></div>
<div class="abs account-links"><span>Login</span><span>|</span><span>Sign Up</span></div>

<header class="abs masthead" role="img" aria-label="Warm wooden plank texture"></header>
<div class="abs brand">Sunward Supper Kits</div>
<nav class="abs main-nav">
  <a class="active">Home</a><a>About Us</a><a>Meal Plans</a><a>How it Works</a><a style="margin-right:0">Contact Us</a>
</nav>

<section class="abs hero"></section>
<div class="abs hero-frame">
  <div class="hero-photo" role="img" aria-label="Photo of sliced grilled chicken on a fresh salad with tomatoes, cucumber and basil on a white platter, with the brand name in orange script beneath"></div>
</div>
<div class="abs slider-dots"><span class="on"></span><span></span><span></span><span></span></div>

<div class="abs feature" style="left:105px">
  <div class="feature-head">
    <svg width="34" height="24" viewBox="0 0 34 24"><path d="M3 20 A14 14 0 0 1 31 20 Z" fill="#ee7f2d"/><circle cx="17" cy="5" r="2.2" fill="#ee7f2d"/><rect x="1" y="20" width="32" height="2.5" rx="1" fill="#ee7f2d"/></svg>
    <span class="feature-title">ABOUT US</span>
  </div>
  <p>Curabitur elementum cursus eros, sit amet vulputate augue. Praesent egestas, orci non iaculis congue, erat massa fringilla libero, ac elementum leo ipsum ac ipsum. Vestibulum porttitor posuere hendrerit. Aliquam faucibus nibh ut mollis pharetra. Sed quis ipsum sed velit consequat venenatis sed ac lectus. Sed vel tellus at risus blandit iaculis. Duis vestibulum, diam a rutrum cursus, purus magna venenatis felis, eget mollis eros lorem at ipsum. Etiam id ultricies dui, sit amet posuere nulla.</p>
</div>

<div class="abs feature" style="left:362px">
  <div class="feature-head">
    <svg width="34" height="28" viewBox="0 0 34 28"><circle cx="17" cy="14" r="10" fill="none" stroke="#ee7f2d" stroke-width="2.5"/><circle cx="17" cy="14" r="6" fill="none" stroke="#ee7f2d" stroke-width="1.5"/><rect x="1" y="2" width="2.2" height="24" rx="1" fill="#ee7f2d"/><path d="M31 2 q-3 6 0 12 v12 h2 V2 z" fill="#ee7f2d"/></svg>
    <span class="feature-title">MEAL PLANS</span>
  </div>
  <p>Curabitur elementum cursus eros, sit amet vulputate augue. Praesent egestas, orci non iaculis congue, erat massa fringilla libero, ac elementum leo ipsum ac ipsum. Vestibulum porttitor posuere hendrerit. Aliquam faucibus nibh ut mollis pharetra. Sed quis ipsum sed velit consequat venenatis sed ac lectus. Sed vel tellus at risus blandit iaculis. Duis vestibulum, diam a rutrum cursus, purus magna venenatis felis, eget mollis eros lorem at ipsum. Etiam id ultricies dui, sit amet posuere nulla.</p>
</div>

<div class="abs feature" style="left:613px">
  <div class="feature-head">
    <svg width="28" height="28" viewBox="0 0 28 28"><path d="M5 2 q2 2 0 4 M9 2 q2 2 0 4" stroke="#ee7f2d" stroke-width="1" fill="none"/><path d="M6 12 h20 q0 8 -10 8 q-10 0 -10 -8z" fill="#ee7f2d"/><ellipse cx="6" cy="23" rx="4" ry="2.2" fill="#ee7f2d"/><rect x="9" y="22" width="17" height="1.6" fill="#ee7f2d"/></svg>
    <span class="feature-title">HOW IT WORKS</span>
  </div>
  <p>Curabitur elementum cursus eros, sit amet vulputate augue. Praesent egestas, orci non iaculis congue, erat massa fringilla libero, ac elementum leo ipsum ac ipsum. Vestibulum porttitor posuere hendrerit. Aliquam faucibus nibh ut mollis pharetra. Sed quis ipsum sed velit consequat venenatis sed ac lectus. Sed vel tellus at risus blandit iaculis. Duis vestibulum, diam a rutrum cursus, purus magna venenatis felis, eget mollis eros lorem at ipsum. Etiam id ultricies dui, sit amet posuere nulla.</p>
</div>

<div class="abs double-rule" style="top:752px"></div>
<h1 class="abs welcome-title" style="font-weight:400">Welcome to Sunward Supper Kits</h1>
<p class="abs welcome-text">Mentum mauris. orbi vulputate ultrices semper. Phasellus ultricies elit et orcidunt est congue&nbsp; tortor vehicul acilisis purus in malesuada purus lacin Mentum mauris. orbi vulputate ultrices semper. Phasellus ultricies elit et orcidunt est congue&nbsp; tortor vehicul acilisis purus in malesuada purus lacin Mentum mauris. orbi vulputate ultrices semper. Phasellus ultricies elit et orcidunt est congue tortor vehicul acilisis purus in malesuada purus lacin Mentum mauris. orbi vulputate ultrices semper. Phasellus ultricies elit et orcidunt est congue tortor vehicul acilisis purus in malesuada purus lacin&nbsp; Mentum mauris. orbi vulputate ultrices semper. Phasellus ultricies elit et orcidunt est congue</p>
<div class="abs double-rule" style="top:905px"></div>

<footer class="abs footer"></footer>
<h2 class="abs footer-heading" style="left:102px;font-weight:400">Contact</h2>
<h2 class="abs footer-heading" style="left:290px;font-weight:400">Get a Free Meal Plan</h2>
<h2 class="abs footer-heading" style="left:478px;font-weight:400">Signup for News Letter</h2>
<h2 class="abs footer-heading" style="left:666px;font-weight:400">Join Us</h2>

<div class="abs contact-row" style="top:1027px">
  <svg width="9" height="9" viewBox="0 0 10 10"><path d="M2 1 l2 2 -1 1.5 q1 2 2.5 2.5 l1.5 -1 2 2 -1.5 1.5 q-4 0 -7 -6z" fill="#ee7f2d"/></svg>
  <span>Phone : (000)&nbsp; 5555 55555</span>
</div>
<div class="abs contact-row" style="top:1045px">
  <svg width="9" height="8" viewBox="0 0 10 8"><rect width="10" height="8" rx="1" fill="#ee7f2d"/><path d="M0.5 1 L5 4.5 9.5 1" stroke="#fff" fill="none"/></svg>
  <span>Email : info@sunwardsupperkits.example</span>
</div>

<div class="abs field" style="top:1032px">Name</div>
<div class="abs field" style="top:1056px">Phone No</div>
<div class="abs field" style="top:1080px">Email</div>
<div class="abs small-btn">Subscribe</div>

<div class="abs news-field"></div>
<div class="abs news-btn">Subscribe</div>

<div class="abs social" style="left:666px" aria-label="Social link"></div>
<div class="abs social" style="left:698px" aria-label="Social link"></div>
<div class="abs social" style="left:729px" aria-label="Social link"></div>
<div class="abs social" style="left:760px" aria-label="Social link"></div>
<div class="abs social" style="left:791px" aria-label="Social link"></div>

<div class="abs copyright">Copyright (c) Sunward Supper Kits&nbsp; |&nbsp; All rights reserved</div>

</body>
</html>
```